Business Card Design - Commercial Photographer

Professional Photographer requires eye catching creative business card. The design will need to incorporate my current logo in some form & not clash with my website tones & colours ( although website will be re designed in the future ). I'm currently shooting new folios in Commercial, Fashion & Architecture so I'm marketing to professional clients rather than portrait / wedding clients. Looking for something professional & creative.

Industry/Entity Type

Marketing

Requirements
Must have
• Website address - www.brightmarrowlens.com.au

Phone number - 0452786104

Email - info@brightmarrowlens.com.au

```html
<!DOCTYPE html>
<html lang="en">
<head>
<meta charset="utf-8">
<title>Bright Marrow Lens Photography – Business Card</title>
<link rel="stylesheet" href="https://fonts.googleapis.com/css2?family=Open+Sans:wght@400;700&display=swap">
<style>
  :root {
    --page-bg: #e9e7e3;
    --card-black: #050505;
    --card-gloss: #2a2a2a;
    --card-white: #f4f4f4;
    --swoosh-grey: #c9c9c9;
    --text-light: #ffffff;
    --text-muted: #bdbdbd;
    --text-dark: #1a1a1a;
    --mark-grey: #5a5a5a;
  }
  * { box-sizing: border-box; margin: 0; padding: 0; }
  html, body {
    width: 1200px; height: 913px; overflow: hidden;
    background: var(--page-bg);
    font-family: "Open Sans", Arial, sans-serif;
  }
  .sheet {
    width: 1200px; height: 913px;
    display: flex; align-items: center; justify-content: center; gap: 40px;
  }
  .card {
    position: relative;
    width: 560px; height: 320px;
    border-radius: 4px;
    overflow: hidden;
    box-shadow: 0 10px 28px rgba(0,0,0,.28);
    background: linear-gradient(125deg, var(--card-black) 0%, var(--card-gloss) 38%, var(--card-black) 60%, var(--card-black) 100%);
  }
  .brand {
    position: absolute;
    display: flex; align-items: center; gap: 14px;
  }
  .brand-mark {
    width: 64px; height: 64px;
    background: var(--mark-grey);
    transform: rotate(-8deg);
    flex: none;
  }
  .brand-name {
    color: var(--text-light);
    font-weight: 700;
    font-size: 24px;
    line-height: 1.1;
    letter-spacing: .02em;
    text-transform: uppercase;
  }
  .card-front .brand { left: 120px; top: 124px; }
  .card-back .swoosh { position: absolute; inset: 0; }
  .card-back .brand { left: 28px; top: 106px; gap: 12px; }
  .card-back .brand-name { font-size: 17px; }
  .card-back .brand-mark { width: 44px; height: 44px; }
  .holder {
    position: absolute; right: 20px; top: 8px; text-align: right;
  }
  .holder-name { color: var(--text-light); font-weight: 700; font-size: 14px; }
  .holder-role { color: var(--text-muted); font-size: 10px; }
  .contact-list {
    position: absolute; right: 18px; top: 120px;
    list-style: none; text-align: right;
    color: var(--text-dark); font-size: 11.5px; line-height: 19px;
  }
  .contact-list li { display: flex; justify-content: flex-end; align-items: center; gap: 7px; }
  .contact-list svg { width: 10px; height: 10px; fill: var(--text-dark); flex: none; }
</style>
</head>
<body>
<main class="sheet">
  <section class="card card-front">
    <div class="brand">
      <div class="brand-mark"></div>
      <div class="brand-name">Bright Marrow Lens<br>Photography</div>
    </div>
  </section>

  <section class="card card-back">
    <svg class="swoosh" viewBox="0 0 560 320" aria-hidden="true">
      <path d="M0 320 L0 300 C150 298 240 268 268 190 C290 110 320 52 420 42 L560 42 L560 320 Z" fill="var(--card-white)"/>
      <path d="M0 292 C140 290 226 262 252 190 C274 108 304 56 410 44" fill="none" stroke="var(--card-black)" stroke-width="6"/>
      <path d="M30 314 C170 308 256 276 282 196 C302 120 330 66 430 52" fill="none" stroke="var(--card-black)" stroke-width="4"/>
      <path d="M80 318 C210 314 282 286 304 206 C322 134 350 80 450 64" fill="none" stroke="var(--swoosh-grey)" stroke-width="3"/>
    </svg>

    <div class="brand">
      <div class="brand-mark"></div>
      <div class="brand-name">Bright Marrow<br>Lens<br>Photography</div>
    </div>

    <div class="holder">
      <div class="holder-name">Your Long Name</div>
      <div class="holder-role">Managing Director</div>
    </div>

    <ul class="contact-list">
      <li>00.00.00.0000
        <svg viewBox="0 0 10 10"><path d="M2 0h2l1 3-1.5 1a6 6 0 0 0 2.5 2.5L7 5l3 1v2a2 2 0 0 1-2 2A8 8 0 0 1 0 2a2 2 0 0 1 2-2z"/></svg></li>
      <li>00.00.00.0000
        <svg viewBox="0 0 10 10"><rect x="2" y="0" width="6" height="3"/><rect x="0" y="4" width="10" height="5"/></svg></li>
      <li>www.yourwebsite.com
        <svg viewBox="0 0 10 10"><circle cx="5" cy="5" r="5"/></svg></li>
      <li>yourname@yourwebsite.com
        <svg viewBox="0 0 10 10"><path d="M0 2h10v6H0z M0 2l5 3.5L10 2"/></svg></li>
      <li>Your Commercial or office address
        <svg viewBox="0 0 10 10"><path d="M5 0a3.5 3.5 0 0 1 3.5 3.5C8.5 6 5 10 5 10S1.5 6 1.5 3.5A3.5 3.5 0 0 1 5 0z"/></svg></li>
    </ul>
  </section>
</main>
</body>
</html>
```